Quovix Pinbrook Page, Post and ADV Format

Quovix.net is a startup that has developed a plugin for e-commerce which understands pinbrook users engagement and gives them an economic value users can spend as discount on e-commerce partners. We are now changing our brand identity and you can see more about our goals in the attachment. WE NEED this Pinbrook contents:
– quotes (layout of images with texts)
– real time marketing
– gif of products you offer
– about us images
– carousel ads/posts
-- cover

. Complete Brief and brand identity is detailed in the attachment.

Target Market(s)

B2B and B2C. Pinbrook users and e-commerce managers.

Industry/Entity Type

It Company

Requirements
Must have
• Pinbrook contents:
• – quotes (layout of images with texts)
• – real time marketing
• – gif of products you offer
• – about us images
• – carousel ads/posts
• -- cover

```html
<!DOCTYPE html>
<html lang="en">
<head>
<meta charset="utf-8">
<title>Quovix Pinbrook Cover Set</title>
<link rel="stylesheet" href="https://fonts.googleapis.com/css2?family=Roboto+Condensed:wght@300;400&family=Nunito:wght@700&display=swap">
<style>
  :root {
    --canvas: #e6e7ea;
    --quote: #ffffff;
    --brand-blue: #16a4ea;
    --shadow: rgba(0, 0, 0, 0.18);
  }
  * { box-sizing: border-box; margin: 0; padding: 0; }
  html, body { width: 1200px; height: 1200px; overflow: hidden; background: var(--canvas); }
  .cover-set {
    width: 1200px; height: 1200px;
    display: flex; flex-direction: column; justify-content: space-evenly; align-items: center;
  }
  .cover {
    position: relative; width: 1000px; height: 370px; overflow: hidden;
    box-shadow: 0 6px 18px var(--shadow);
  }
  .cover-photo { position: absolute; inset: 0; }
  .cover--camera .cover-photo {
    background:
      radial-gradient(ellipse 28% 45% at 78% 55%, rgba(20,18,22,0.85), transparent 70%),
      linear-gradient(100deg, #7a3f8c 0%, #b33a6e 22%, #c7613f 40%, #5c8c8a 58%, #4b5c8f 78%, #38335a 100%);
  }
  .cover--speaker .cover-photo {
    background:
      radial-gradient(ellipse 22% 40% at 82% 45%, rgba(235,240,245,0.8), transparent 70%),
      radial-gradient(ellipse 18% 35% at 66% 62%, rgba(30,45,70,0.7), transparent 70%),
      linear-gradient(100deg, #6a9a7c 0%, #3f8ea6 25%, #2f74b8 45%, #4d8bb0 65%, #2c4f86 100%);
  }
  .cover--dining .cover-photo {
    background:
      radial-gradient(ellipse 30% 40% at 75% 60%, rgba(225,220,215,0.75), transparent 70%),
      radial-gradient(ellipse 40% 30% at 72% 92%, rgba(120,60,25,0.8), transparent 70%),
      linear-gradient(100deg, #7d5a79 0%, #8c5e4a 25%, #9a7b55 45%, #6d5240 65%, #4a3a30 100%);
  }
  .quote {
    position: absolute; left: 52px; top: 38px;
    font-family: "Roboto Condensed", sans-serif; font-weight: 300;
    font-size: 29px; line-height: 44px; letter-spacing: 2.5px;
    color: var(--quote); text-transform: uppercase;
    text-shadow: 0 1px 3px rgba(0,0,0,0.25);
  }
  .brand-mark {
    position: absolute; left: 430px; top: 150px;
    display: flex; flex-direction: column; align-items: center; gap: 10px;
  }
  .brand-dot { width: 86px; height: 86px; border-radius: 50%; background: var(--brand-blue); border: 5px solid #ffffff; }
  .brand-name {
    font-family: "Nunito", sans-serif; font-weight: 700; font-size: 34px;
    color: var(--brand-blue); letter-spacing: 1px;
  }
</style>
</head>
<body>
<main class="cover-set">
  <section class="cover cover--camera">
    <div class="cover-photo" role="img" aria-label="Blurred colourful background with a close-up of a DSLR camera and lens on the right"></div>
    <p class="quote">"Quality is more important then quantity.<br>One home run is much better than two doubles."<br>- Stefan Joris</p>
    <div class="brand-mark"><span class="brand-dot"></span><span class="brand-name">quovix</span></div>
  </section>
  <section class="cover cover--speaker">
    <div class="cover-photo" role="img" aria-label="Soft blue-green blurred background with a white loudspeaker and small figurine on a desk"></div>
    <p class="quote">"Quality is more important then quantity.<br>One home run is much better than two doubles."<br>- Stefan Joris</p>
    <div class="brand-mark"><span class="brand-dot"></span><span class="brand-name">quovix</span></div>
  </section>
  <section class="cover cover--dining">
    <div class="cover-photo" role="img" aria-label="Warm blurred background with white chairs around a wooden dining table"></div>
    <p class="quote">"Quality is more important then quantity.<br>One home run is much better than two doubles."<br>- Stefan Joris</p>
    <div class="brand-mark"><span class="brand-dot"></span><span class="brand-name">quovix</span></div>
  </section>
</main>
</body>
</html>
```